Casa Vero Inspections Business Card

I need a business card for my new company. The company is going to provide home inspections. The name of the company is Casa Vero Inspections. I am not sure if I want a single sided card or a double. I have a logo already that I want to incorporate into the card design. I was wondering if I should incorporate a catch phrase on my card or not. If I did the phrase would be "The Intelligent Choice for Home Inspections" but i am unsure how or if to use it on a card. The following information needs to be on the card.
Home Inspection
My Name: Marcus T. Wolford Phone Number: 555-301-7762 Email: mwolford@casaveroinspections.com Website: www.casaveroinspections.com NY HI License # 27300519462

```html
<!DOCTYPE html>
<html lang="en">
<head>
<meta charset="utf-8">
<title>Casa Vero Inspections Business Card</title>
<link rel="stylesheet" href="https://fonts.googleapis.com/css2?family=Montserrat:wght@600;800&family=Open+Sans:wght@400;600&display=swap">
<style>
  :root {
    --brand-blue: #1a78b8;
    --brand-blue-deep: #0f63a0;
    --brand-navy: #0d5a92;
    --paper: #f4f5f6;
    --rule-grey: #8e9194;
    --text-grey: #6b6e72;
    --stage: #e6e8ea;
    --white: #ffffff;
  }
  * { margin: 0; padding: 0; box-sizing: border-box; }
  html, body { width: 1200px; height: 900px; overflow: hidden; }
  body {
    background: var(--stage);
    position: relative;
    font-family: "Open Sans", Arial, sans-serif;
  }
  .card {
    position: absolute;
    left: 320px;
    width: 560px;
    height: 320px;
    overflow: hidden;
    box-shadow: 0 6px 18px rgba(0,0,0,0.18);
  }
  .card--front { top: 90px; background: var(--paper); }
  .card--back {
    top: 490px;
    background: linear-gradient(135deg, var(--brand-blue) 0%, var(--brand-blue-deep) 100%);
    display: flex;
    align-items: center;
    justify-content: center;
  }
  .front__header {
    height: 130px;
    position: relative;
  }
  .person {
    position: absolute;
    left: 40px;
    top: 78px;
  }
  .person__name {
    font-family: "Montserrat", Arial, sans-serif;
    font-weight: 800;
    font-size: 19px;
    color: var(--brand-navy);
    letter-spacing: 0.5px;
    text-transform: uppercase;
  }
  .person__title {
    font-size: 15px;
    color: var(--text-grey);
    margin-top: 1px;
  }
  .brand {
    position: absolute;
    right: 36px;
    top: 34px;
    display: flex;
    align-items: center;
    gap: 10px;
  }
  .brand__mark {
    width: 14px; height: 14px;
    background: var(--brand-navy);
  }
  .brand__name {
    font-family: "Montserrat", Arial, sans-serif;
    font-weight: 800;
    font-size: 20px;
    color: var(--brand-navy);
    text-transform: uppercase;
    letter-spacing: 0.5px;
  }
  .front__rule {
    height: 10px;
    background: linear-gradient(90deg, var(--rule-grey), #c3c5c7 60%, var(--rule-grey));
  }
  .front__body {
    height: 180px;
    background: linear-gradient(135deg, var(--brand-blue) 0%, var(--brand-blue-deep) 100%);
    padding: 38px 0 0 46px;
    color: var(--white);
  }
  .contact { list-style: none; font-size: 14px; line-height: 25px; }
  .contact li { display: flex; align-items: center; gap: 10px; }
  .contact svg { width: 14px; height: 14px; flex: none; }
  .contact .license { padding-left: 24px; }
  .card--back .brand { position: static; }
  .card--back .brand__mark { background: var(--white); width: 20px; height: 20px; }
  .card--back .brand__name { color: var(--white); font-size: 30px; }
</style>
</head>
<body>
  <section class="card card--front" aria-label="Business card front">
    <div class="front__header">
      <div class="person">
        <div class="person__name">Marcus T. Wolford</div>
        <div class="person__title">President</div>
      </div>
      <div class="brand">
        <span class="brand__mark"></span>
        <span class="brand__name">Casa Vero Inspections</span>
      </div>
    </div>
    <div class="front__rule"></div>
    <div class="front__body">
      <ul class="contact">
        <li>
          <svg viewBox="0 0 16 16" aria-hidden="true"><path fill="#fff" d="M3.5 1.5l2.3 0 1 3.2-1.5 1.2a8 8 0 0 0 4.8 4.8l1.2-1.5 3.2 1v2.3c0 .8-.7 1.5-1.5 1.5C6.8 14 2 9.2 2 3c0-.8.7-1.5 1.5-1.5z"/></svg>
          555-301-7762
        </li>
        <li>
          <svg viewBox="0 0 16 16" aria-hidden="true"><rect x="1" y="3" width="14" height="10" rx="1" fill="#fff"/><path d="M1.5 3.8L8 8.8l6.5-5" stroke="#1a78b8" stroke-width="1.4" fill="none"/></svg>
          mwolford@casaveroinspections.com
        </li>
        <li>
          <svg viewBox="0 0 16 16" aria-hidden="true"><g fill="none" stroke="#fff" stroke-width="1.3"><circle cx="8" cy="8" r="6.5"/><ellipse cx="8" cy="8" rx="2.8" ry="6.5"/><path d="M1.5 8h13M2.5 4.8h11M2.5 11.2h11"/></g></svg>
          www.casaveroinspections.com
        </li>
        <li class="license">NY HI License # 27300519462</li>
      </ul>
    </div>
  </section>

  <section class="card card--back" aria-label="Business card back">
    <div class="brand">
      <span class="brand__mark"></span>
      <span class="brand__name">Casa Vero Inspections</span>
    </div>
  </section>
</body>
</html>
```